CORWIN HOLT Perfume Bottle Mock-up for assorted Social Media Platforms and Wordpress site

We need a mock-up of branded perfume bottles for inclusion on Social Media platforms and our Wordpress site. At this point in time we need only consider the bottles themselves - outer packaging is not required.

The bottle style is a 10ml tube-drawn clear glass bottle, stainless steel roller-ball applicator and matt white aluminium overcap. The dimensions of the bottle are as follows - 80mm long (base to neck) and approximately 15mm diameter. The cap is 25mm long with diameter to fit the bottle. Images of the actual bottle and cap (in gold - not matt white) are attached for your reference - the quality of the images is low and most likely inappropriate for reproduction but they will give you a good idea of the proportions we have to work with.

The label will be white with the CORWIN HOLT logo printed in black - also included on the mock-up will be the words "parfum extrait" to denote the product strength along with the scent name. The preferred font for this text is Helvetica and we’d like to see a range of upper, lower and sentence case options.

We have two logo designs to choose from – 2 lines and 3 lines. JPEGS of each of the logos in black are attached. If you need another format to work with please advise asap.

We would like to break up the monochromatic theme with a dash of rich pinky red - Pantone 226 is our preferred shade. This could be incorporated via some sort of basic graphical element or by printing the scent name in this shade - we are undecided and would therefore like to look at some ideas.

We have attached images of a similarly sized niche prestige fragrance product from the Tobias Renfrew brand - this will give you an idea of the type of minimalist aesthetics we are aiming for. Also included is a group packaging shot so you can see how the design is reworked for larger/different products.

Please be advised that we have 3 scent names that we need to mock up – more may follow.

chasing the lantern
silver never sleeps
l'ombre de minuit

Finally, please be advised that the perfume liquid itself will be a golden, ambery hue.

If you need anything further from us in order to get started, please don't hesitate to let to us know.

Kindest Regards,
Tess

Hello everyone,

Brief has been updated slightly with the inclusion of eps and ai logo files.

Cheers,
Tess

Hello again everyone,

Please note (as per the brief) that the overcap on the bottle will be be matt white aluminium - not gold - and we are going to be labeling the bottles - not printing them. 

We would also like to look at both white and black label options.  An image of a limited edition Vonteli fragrance with a white cap and black label is included for your reference.

Cheers,
Tess

Hello again,

We've posted a couple more images to help you get a feel for the brand - a minimalist/urban painted white brick wall and a Melbourne laneway covered in graffiti.

Cheers,
Tess

Target Market(s)

Inspired by authentic creation and enduring beauty, the CORWIN HOLT client values the art and science of perfumery and relishes in the freedom of self-expression. Our network of boutique retailers is similarly discerning. Favouring quality over quantity and sincerity over sensation, we work with only with the most ardent and inspired fragrance merchants.

Industry/Entity Type

Printing

Font styles to use
Sans Serif

Requirements
Must have
• The design should have a clean, unisex, minimalist style.
Should not have
• Anything flowery - serif, decorative or script fonts are a no-go.

```html
<!DOCTYPE html>
<html lang="en">
<head>
<meta charset="utf-8">
<title>Corwin Holt – parfum extrait rollerball bottles</title>
<link rel="stylesheet" href="https://fonts.googleapis.com/css2?family=Arimo:wght@400;700&display=swap">
<style>
  :root {
    --backdrop: #231f20;
    --cap: #ffffff;
    --cap-shade: #e4e4e4;
    --glass-edge: #d8d2b8;
    --amber-deep: #a8913a;
    --amber: #d6c470;
    --amber-light: #eee3a6;
    --label: #ffffff;
    --ink: #2b2b2b;
    --rule: #9a9a9a;
    --accent: #e0245e;
  }
  * { margin: 0; padding: 0; box-sizing: border-box; }
  html, body {
    width: 1200px;
    height: 1000px;
    overflow: hidden;
    background: var(--backdrop);
    font-family: "Arimo", Helvetica, Arial, sans-serif;
  }
  .stage {
    position: relative;
    width: 1200px;
    height: 1000px;
  }

  /* bottle */
  .bottle {
    position: absolute;
    top: 138px;
    width: 100px;
    height: 780px;
  }
  .bottle--lantern { left: 434px; }
  .bottle--silver  { left: 557px; }
  .bottle--minuit  { left: 680px; }

  .bottle__cap {
    position: absolute;
    top: 0;
    left: 0;
    width: 100px;
    height: 196px;
    border-radius: 10px 10px 2px 2px;
    background: linear-gradient(90deg, var(--cap-shade) 0%, var(--cap) 18%, var(--cap) 78%, var(--cap-shade) 100%);
  }
  .bottle__glass {
    position: absolute;
    top: 195px;
    left: 6px;
    width: 88px;
    height: 488px;
    border-radius: 0 0 24px 24px;
    border-top: 8px solid var(--glass-edge);
    background: linear-gradient(90deg, var(--amber-deep) 0%, var(--amber) 14%, var(--amber-light) 40%, var(--amber) 75%, var(--amber-deep) 100%);
  }
  .bottle__reflection {
    position: absolute;
    top: 688px;
    left: 6px;
    width: 88px;
    height: 90px;
    border-radius: 24px 24px 0 0;
    background: linear-gradient(180deg, rgba(214, 196, 112, 0.28) 0%, rgba(214, 196, 112, 0) 100%);
  }

  /* label */
  .label {
    position: absolute;
    top: 242px;
    left: 14px;
    width: 70px;
    height: 318px;
    background: var(--label);
    color: var(--ink);
  }
  .label__names {
    position: absolute;
    top: 24px;
    left: 8px;
    height: 196px;
    writing-mode: vertical-rl;
    transform: rotate(180deg);
    display: flex;
    flex-direction: column;
  }
  .label__brand {
    font-weight: 700;
    font-size: 25px;
    letter-spacing: 1px;
    line-height: 30px;
    white-space: nowrap;
    padding-left: 4px;
  }
  .label__scent {
    font-size: 15px;
    line-height: 24px;
    white-space: nowrap;
    border-right: 1px solid var(--rule);
    padding-right: 4px;
  }
  .label__strength {
    position: absolute;
    top: 234px;
    left: 0;
    width: 100%;
    text-align: center;
    font-size: 18px;
    line-height: 25px;
  }
  .label__mark {
    position: absolute;
    top: 292px;
    right: 8px;
    width: 18px;
    height: 18px;
    background: var(--accent);
  }
</style>
</head>
<body>
  <main class="stage">
    <article class="bottle bottle--lantern">
      <div class="bottle__cap"></div>
      <div class="bottle__glass"></div>
      <div class="bottle__reflection"></div>
      <section class="label">
        <div class="label__names">
          <span class="label__brand">CORWIN HOLT</span>
          <span class="label__scent">chasing the lantern</span>
        </div>
        <p class="label__strength">parfum<br>extrait</p>
        <div class="label__mark" role="img" aria-label="Small rich pinky red emblem"></div>
      </section>
    </article>

    <article class="bottle bottle--silver">
      <div class="bottle__cap"></div>
      <div class="bottle__glass"></div>
      <div class="bottle__reflection"></div>
      <section class="label">
        <div class="label__names">
          <span class="label__brand">CORWIN HOLT</span>
          <span class="label__scent">silver never sleeps</span>
        </div>
        <p class="label__strength">parfum<br>extrait</p>
        <div class="label__mark" role="img" aria-label="Small rich pinky red emblem"></div>
      </section>
    </article>

    <article class="bottle bottle--minuit">
      <div class="bottle__cap"></div>
      <div class="bottle__glass"></div>
      <div class="bottle__reflection"></div>
      <section class="label">
        <div class="label__names">
          <span class="label__brand">CORWIN HOLT</span>
          <span class="label__scent">l'ombre de minuit</span>
        </div>
        <p class="label__strength">parfum<br>extrait</p>
        <div class="label__mark" role="img" aria-label="Small rich pinky red emblem"></div>
      </section>
    </article>
  </main>
</body>
</html>
```